Consulting company requires a logo and business card design

I require a logo/business card design for a new company based in Sexsmith Alberta called TanRidge Field Advisory Ltd. I plan to provide the following services: Construction management/inspection for the oil and gas industry, as well as general consulting for Asset Management, fleet management, etc. Have attached a copy of resume for use as guide for

Target Market(s)

Businesses within the oil and gas production, construction and shipping industry

Industry/Entity Type

Oil And Gas

Contact Information for Business Card

Believe should highlight, services offered, safety, quality,

Logo Text

TanRidge Field Advisory (TRFA) ?

Font styles to use
Script

Requirements
Must have
• Open to all options

```html
<!DOCTYPE html>
<html lang="en">
<head>
<meta charset="utf-8">
<title>TanRidge Field Advisory Ltd. – Business Card</title>
<link rel="stylesheet" href="https://fonts.googleapis.com/css2?family=Open+Sans:wght@400;600;700&display=swap">
<style>
  :root {
    --stage: #2b2b2d;
    --card: #1f2122;
    --card-edge: #2a2c2d;
    --green: #5fbf3a;
    --green-deep: #2f8a2a;
    --text: #f2f2f2;
    --muted: #cfd2d0;
  }
  * { box-sizing: border-box; margin: 0; padding: 0; }
  html, body {
    width: 1200px; height: 1189px; overflow: hidden;
    background: var(--stage);
    font-family: "Open Sans", Arial, sans-serif;
  }
  .canvas {
    position: relative; width: 1200px; height: 1189px;
    display: flex; flex-direction: column; align-items: center; justify-content: center; gap: 70px;
  }
  .card {
    position: relative; width: 880px; height: 503px;
    background: var(--card);
    border-radius: 26px;
    box-shadow: 0 18px 40px rgba(0,0,0,.45);
    overflow: hidden;
  }
  /* Front */
  .card--front { padding: 70px 80px; display: flex; flex-direction: column; align-items: center; text-align: center; }
  .wordmark { color: var(--green); font-weight: 600; letter-spacing: .5px; }
  .card--front .wordmark { font-size: 44px; margin-top: 20px; }
  .competencies-title {
    margin-top: 70px; color: var(--green); font-weight: 700; font-size: 27px; letter-spacing: .5px;
  }
  .competencies { margin-top: 26px; color: var(--text); font-size: 22px; line-height: 1.55; }
  /* Back */
  .card--back { display: flex; }
  .brand-side {
    width: 48%; display: flex; align-items: center; justify-content: center; padding-left: 40px;
  }
  .brand-side .wordmark { font-size: 30px; display: flex; align-items: center; gap: 12px; line-height: 1.2; }
  .brand-dot { width: 16px; height: 16px; border-radius: 50%; background: var(--green); flex: none; }
  .divider {
    width: 2px; margin: 70px 0; background: linear-gradient(var(--green-deep), rgba(47,138,42,.3));
  }
  .contact-side { flex: 1; padding: 100px 40px 0 50px; color: var(--text); }
  .person { color: var(--green); font-weight: 700; font-size: 30px; letter-spacing: .5px; }
  .address { margin-top: 60px; font-size: 23px; line-height: 1.3; }
  .contact-line { display: flex; align-items: center; gap: 12px; font-size: 23px; margin-top: 6px; }
  .icon { width: 28px; height: 28px; flex: none; }
</style>
</head>
<body>
<main class="canvas">
  <section class="card card--front">
    <h1 class="wordmark">TanRidge Field Advisory Ltd.</h1>
    <h2 class="competencies-title">CORE COMPETENCIES</h2>
    <p class="competencies">
      Asset management | Strategic Planning | Process Improvement<br>
      Budget Planning &amp; Cost Control | Client Relations | Quality Control<br>
      Fleet Management | Construction Quality Management
    </p>
  </section>

  <section class="card card--back">
    <div class="brand-side">
      <div class="wordmark"><span class="brand-dot"></span><span>TanRidge Field Advisory Ltd.</span></div>
    </div>
    <div class="divider"></div>
    <div class="contact-side">
      <p class="person">DALE MORROW</p>
      <p class="address">RR#4 Ridgeview Alberta,<br>T0K 2L0</p>
      <p class="contact-line">
        <svg class="icon" viewBox="0 0 28 28" aria-hidden="true">
          <rect width="28" height="28" rx="5" fill="#5fbf3a"/>
          <path d="M8 17c0-5 3-8 6-8s6 3 6 8z" fill="#1f2122"/>
          <rect x="6" y="9" width="16" height="3" rx="1.5" fill="#1f2122"/>
          <circle cx="14" cy="15" r="2" fill="#5fbf3a"/>
        </svg>
        (780)555-0148
      </p>
      <p class="contact-line">
        <svg class="icon" viewBox="0 0 28 28" aria-hidden="true">
          <rect width="28" height="28" rx="5" fill="#5fbf3a"/>
          <rect x="6" y="8" width="16" height="12" rx="1" fill="#1f2122"/>
          <path d="M6.5 8.5 14 15l7.5-6.5" stroke="#5fbf3a" stroke-width="1.6" fill="none"/>
        </svg>
        dalemorrow61@mailbox.com
      </p>
    </div>
  </section>
</main>
</body>
</html>
```